Flyer Design Project

I am opening a yoga studio called Willowmere Yoga .Pilates. Fitness
and require a flyer that will be letterbox dropped. It will two sided - DL size.100mm × 210mm

The studio will offer Vinyasa Flow Yoga and Mat Pilates classes. We aim to enable people to lead healthier, happier lives through improved strength, flexibility and general well being that regular yoga and pilates practice offers.

We offer group classes, private and semi private sessions in yoga and pilates.

it must have the logo on it- I have uploaded the logo in two versions - not sure what will look the best.

pick up one of the colours from the logo as the background colour.

Side one:
Simple and clean with one side showing logo and address details, website and with simple intro about studio (if it fits)

Location: 1st Floor, 17 Larkspur Parade, Tindale, 3286
phone: 0428 596143
www.willowmeretindale.com.au

OPENING OCTOBER

other side - class descriptions and intro offer for new clients
$20 for 7 days of classes
$99 for 1 month unlimited.

Class descriptions:
Vinyasa Flow yoga: A class that flows from pose to pose integrating breath, alignment, strength and power. All levels are catered for in a warm room heated to around 26 degrees. You will leave feeling inspired, empowered and energised.

Mat Pilates: A strong, challenging class integrating the key principles of pilates: concentration, control, centring, precision, flowing movement and breath. Using the core as a focus to develop these principles you will be hooked on the physical freedom you experience post workout:improved strength, flexibility and vitality that pilates offers.

Private and semi Private tuition available.

Target Market(s)

mainly women, athletic, 35-55 age, middle class, well educated

Industry/Entity Type

Fitness

Requirements
Must have
• 2 pages
the logo

Should not have
• no pics

```html
<!DOCTYPE html>
<html lang="en">
<head>
<meta charset="utf-8">
<title>Willowmere Yoga DL Flyer</title>
<link href="https://fonts.googleapis.com/css2?family=PT+Sans:wght@400;700&family=PT+Sans+Narrow:wght@700&display=swap" rel="stylesheet">
<style>
  :root {
    --backdrop: #4a3324;
    --sky: #1cb5e8;
    --sun-yellow: #f5ec23;
    --olive-ink: #3a3416;
    --charcoal: #3b3b3d;
    --band-grey: #5f6062;
    --flyer-red: #ee1d23;
    --white: #ffffff;
    --stripe-yellow: #f6e43a;
    --stripe-grey: #b9bbbd;
    --stripe-blue: #7ecbe8;
    --name-grey: #5b5b5d;
  }
  * { box-sizing: border-box; margin: 0; padding: 0; }
  html, body {
    width: 1200px; height: 1112px; overflow: hidden;
    background: var(--backdrop);
    font-family: "PT Sans", Arial, sans-serif;
  }
  .canvas { position: relative; width: 1200px; height: 1112px; }

  .flyer {
    position: absolute; top: 94px; width: 445px; height: 934px;
    overflow: hidden; background: var(--flyer-red);
    box-shadow: 0 6px 18px rgba(0,0,0,.45);
  }
  .flyer--offer { left: 140px; }
  .flyer--cover { left: 612px; }

  .stripes { position: absolute; left: 0; width: 100%; top: 446px; height: 22px; }

  /* ---------- offer side ---------- */
  .offer-panel {
    position: absolute; left: 0; top: 0; width: 100%; height: 381px;
    background: var(--sky);
  }
  .offer-badge {
    position: absolute; left: 31px; top: 17px; width: 383px; height: 136px;
    background: var(--sun-yellow); border-radius: 16px;
    box-shadow: 0 10px 10px -6px rgba(0,0,0,.35);
    display: flex; flex-direction: column; align-items: center; justify-content: center;
    font-family: "PT Sans Narrow", "Arial Narrow", sans-serif; font-weight: 700;
    color: var(--olive-ink); font-size: 55px; line-height: 56px;
  }
  .offer-price {
    position: absolute; left: 0; width: 100%; text-align: center;
    font-family: "PT Sans Narrow", "Arial Narrow", sans-serif; font-weight: 700;
    color: var(--charcoal); font-size: 36px; line-height: 42px;
  }
  .offer-price--week { top: 176px; }
  .offer-price--month { top: 282px; }
  .offer-rule {
    position: absolute; left: 49px; width: 346px; top: 266px; height: 2px;
    background: rgba(255,255,255,.85);
  }
  .section-band {
    position: absolute; left: 0; top: 381px; width: 100%; height: 65px;
    background: var(--band-grey);
    display: flex; align-items: center; justify-content: center;
    font-family: "PT Sans Narrow", "Arial Narrow", sans-serif; font-weight: 700;
    font-size: 47px; color: var(--white); letter-spacing: -.5px;
    text-shadow: 2px 3px 3px rgba(0,0,0,.55);
  }
  .class-list {
    position: absolute; left: 40px; right: 40px; top: 492px; color: var(--white);
  }
  .class { margin-bottom: 32px; }
  .class__name {
    font-weight: 700; font-size: 18.5px; text-align: center; margin-bottom: 10px;
  }
  .class__text {
    font-size: 15.3px; line-height: 22.2px; text-align: justify;
    text-align-last: center;
  }
  .tuition-pill {
    position: absolute; left: 28px; top: 884px; width: 389px; height: 37px;
    border-radius: 19px; background: var(--sun-yellow);
    display: flex; align-items: center; justify-content: center;
    font-weight: 700; font-size: 17px; color: #111;
  }

  /* ---------- cover side ---------- */
  .cover-top {
    position: absolute; left: 0; top: 0; width: 100%; height: 446px;
    background: var(--white);
  }
  .studio-name {
    position: absolute; left: 40px; right: 40px; top: 160px;
    text-align: center; font-weight: 700; color: var(--name-grey);
    font-size: 34px; line-height: 42px;
  }
  .headline {
    position: absolute; left: 0; width: 100%; top: 500px; text-align: center;
    font-weight: 700; color: var(--white); font-size: 79px; line-height: 84px;
    text-shadow: 2px 3px 4px rgba(0,0,0,.3);
  }
  .contact {
    position: absolute; left: 0; width: 100%; top: 774px; text-align: center;
    color: var(--white);
  }
  .contact__label { font-weight: 700; font-size: 16px; letter-spacing: 1.5px; }
  .contact__phone { font-weight: 700; font-size: 38px; line-height: 46px; margin-top: 6px; }
  .contact__address { font-size: 13.5px; margin-top: 18px; }
  .contact__web { font-weight: 700; font-size: 16px; letter-spacing: 3px; margin-top: 10px; }
</style>
</head>
<body>
<div class="canvas">

  <section class="flyer flyer--offer">
    <div class="offer-panel">
      <div class="offer-badge"><span>Intro OFFER</span><span>for New Clients</span></div>
      <p class="offer-price offer-price--week">$20 for 7 Days<br>of Classes</p>
      <div class="offer-rule"></div>
      <p class="offer-price offer-price--month">$99 for 1 Month<br>Unlimited</p>
    </div>
    <h2 class="section-band">CLASS DESCRIPTIONS</h2>
    <svg class="stripes" viewBox="0 0 445 22" preserveAspectRatio="none" aria-hidden="true">
      <rect width="445" height="22" fill="#fff"/>
      <rect y="0" width="445" height="4" fill="var(--stripe-yellow)"/>
      <rect y="8" width="445" height="4" fill="var(--stripe-grey)"/>
      <rect y="15" width="445" height="4" fill="var(--stripe-blue)"/>
    </svg>
    <div class="class-list">
      <article class="class">
        <h3 class="class__name">Vinyasa Flow yoga:</h3>
        <p class="class__text">A class that flows from pose to pose integrating breath, alignment, strength and power. All levels are catered for in a warm room heated to around 26 degrees. You will leave feeling inspired, empowered and energised.</p>
      </article>
      <article class="class">
        <h3 class="class__name">Mat Pilates:</h3>
        <p class="class__text">A strong, challenging class integrating the key principles of pilates: concentration, control, centring, precision, flowing movement and breath. Using the core as a focus to develop these principles you will be hooked on the physical freedom you experience post workout:improved strength, flexibility and vitality that pilates offers.</p>
      </article>
    </div>
    <div class="tuition-pill">Private and Semi Private Tuition Available</div>
  </section>

  <section class="flyer flyer--cover">
    <div class="cover-top">
      <p class="studio-name">Willowmere Yoga .Pilates. Fitness</p>
    </div>
    <svg class="stripes" viewBox="0 0 445 22" preserveAspectRatio="none" aria-hidden="true">
      <rect width="445" height="22" fill="#fff"/>
      <rect y="0" width="445" height="4" fill="var(--stripe-yellow)"/>
      <rect y="8" width="445" height="4" fill="var(--stripe-grey)"/>
      <rect y="15" width="445" height="4" fill="var(--stripe-blue)"/>
    </svg>
    <h1 class="headline">OPENING<br>OCTOBER</h1>
    <div class="contact">
      <p class="contact__label">CONTACT US</p>
      <p class="contact__phone">0428 596143</p>
      <p class="contact__address">1st Floor, 17 Larkspur Parade, Tindale, 3286</p>
      <p class="contact__web">www.willowmeretindale.com.au</p>
    </div>
  </section>

</div>
</body>
</html>
```